Business card design for Plumbing and Gas fitting company

We need a business card design for our plumbing and gas fitting company using the company logo and director details. Design should be modern and eye-catching however kept reasonably simple. This design should be targeted at commercial businesses/work so professionalism is key.

Target Market(s)

Commercial/business

Industry/Entity Type

Plumbing

Contact Information for Business Card

Warren Dohey
Director
027 581 9043
warren@vantorplumbingandgas.example
PO Box 7816
Palmerston North 4472

Font styles to use
Sans Serif

Requirements
Must have
• Logo
• Modern
• Kept simple
Nice to have
• Colour scheme based around logo

```html
<!DOCTYPE html>
<html lang="en">
<head>
<meta charset="utf-8">
<title>Vantor Plumbing &amp; Gas – Business Card</title>
<link rel="stylesheet" href="https://fonts.googleapis.com/css2?family=Montserrat:wght@700&family=Source+Sans+3:wght@400;700&display=swap">
<style>
  :root {
    --backdrop: #e8e5e0;
    --brand-blue: #0f72bc;
    --brand-orange: #e97b2f;
    --brand-grey: #808080;
    --text-grey: #4a4a4a;
    --card-white: #ffffff;
    --card-black: #000000;
  }
  * { margin: 0; padding: 0; box-sizing: border-box; }
  html, body {
    width: 1200px;
    height: 987px;
    overflow: hidden;
    background: var(--backdrop);
  }
  .canvas {
    position: relative;
    width: 1200px;
    height: 987px;
  }
  .card {
    position: absolute;
    left: 293px;
    width: 615px;
    height: 350px;
    border-radius: 20px;
    overflow: hidden;
    box-shadow: 0 3px 10px rgba(0,0,0,0.25);
  }
  .card-front { top: 131px; background: var(--card-white); }
  .card-back { top: 506px; background: var(--card-black); }

  .front-waves {
    position: absolute;
    inset: 0;
    width: 100%;
    height: 100%;
  }
  .holder {
    position: absolute;
    right: 36px;
    top: 20px;
    text-align: right;
    color: var(--card-white);
    font-family: "Montserrat", sans-serif;
    font-weight: 700;
    font-variant: small-caps;
    letter-spacing: 1px;
  }
  .holder-name { font-size: 24px; line-height: 1.1; }
  .holder-role { font-size: 18px; line-height: 1.2; }

  .brand {
    position: absolute;
    display: flex;
    align-items: center;
    gap: 10px;
  }
  .brand-name {
    font-family: "Source Sans 3", sans-serif;
    font-weight: 700;
    color: var(--brand-blue);
    white-space: nowrap;
  }
  .brand-dot {
    border-radius: 50%;
    background: var(--brand-orange);
    flex: none;
  }
  .card-front .brand { left: 50px; top: 130px; }
  .card-front .brand-name { font-size: 26px; }
  .card-front .brand-dot { width: 22px; height: 22px; }

  .card-back .brand {
    left: 50%;
    top: 50%;
    transform: translate(-50%, -50%);
  }
  .card-back .brand-name { font-size: 36px; }
  .card-back .brand-dot { width: 30px; height: 30px; }

  .contact {
    position: absolute;
    left: 50px;
    top: 235px;
    list-style: none;
    font-family: "Source Sans 3", sans-serif;
    font-size: 17px;
    color: var(--text-grey);
  }
  .contact li {
    display: flex;
    align-items: center;
    gap: 8px;
    height: 25px;
  }
  .contact svg { width: 16px; height: 16px; fill: var(--brand-blue); flex: none; }

  .front-glow {
    position: absolute;
    right: -30px;
    bottom: -40px;
    width: 180px;
    height: 180px;
    border-radius: 50%;
    background: #e3eff9;
    opacity: 0.8;
  }
</style>
</head>
<body>
<main class="canvas">
  <section class="card card-front" aria-label="Business card front">
    <div class="front-glow"></div>
    <svg class="front-waves" viewBox="0 0 525 298" preserveAspectRatio="none" aria-hidden="true">
      <path fill="#808080" d="M300 82 C380 100 450 102 525 92 V108 C450 116 380 112 300 82 Z"/>
      <path fill="#e97b2f" d="M0 135 C20 70 90 20 190 22 C240 23 280 40 300 50 C260 32 150 20 80 60 C40 82 15 110 0 150 Z"/>
      <path fill="#0f72bc" d="M0 0 H525 V96 C450 104 380 96 320 72 C260 46 200 22 140 24 C80 28 30 60 0 92 Z"/>
    </svg>
    <div class="holder">
      <p class="holder-name">Warren Dohey</p>
      <p class="holder-role">Director</p>
    </div>
    <div class="brand">
      <span class="brand-name">Vantor Plumbing &amp; Gas</span>
      <span class="brand-dot"></span>
    </div>
    <ul class="contact">
      <li>
        <svg viewBox="0 0 24 24" aria-hidden="true"><path d="M6.6 10.8a15.1 15.1 0 0 0 6.6 6.6l2.2-2.2c.3-.3.7-.4 1-.2 1.1.4 2.3.6 3.6.6.6 0 1 .4 1 1V20c0 .6-.4 1-1 1A17 17 0 0 1 3 4c0-.6.4-1 1-1h3.5c.6 0 1 .4 1 1 0 1.3.2 2.5.6 3.6.1.3 0 .7-.2 1z"/></svg>
        <span>027 581 9043</span>
      </li>
      <li>
        <svg viewBox="0 0 24 24" aria-hidden="true"><path d="M2 5h20v14H2z M2 5l10 8 10-8" fill="#0f72bc"/><path d="M3 6l9 7 9-7" fill="none" stroke="#fff" stroke-width="1.6"/></svg>
        <span>warren@vantorplumbingandgas.example</span>
      </li>
      <li>
        <svg viewBox="0 0 24 24" aria-hidden="true"><path d="M12 2a7 7 0 0 0-7 7c0 5 7 13 7 13s7-8 7-13a7 7 0 0 0-7-7zm0 9.5A2.5 2.5 0 1 1 12 6.5a2.5 2.5 0 0 1 0 5z"/></svg>
        <span>PO Box 7816, Palmerston North 4472</span>
      </li>
    </ul>
  </section>

  <section class="card card-back" aria-label="Business card back">
    <div class="brand">
      <span class="brand-name">Vantor Plumbing &amp; Gas</span>
      <span class="brand-dot"></span>
    </div>
  </section>
</main>
</body>
</html>
```